Business Card for Multi-Brand Sportswear Company

We are looking for a business card which represents our company and the multiple brands within it.

The company: Kelt Athletic (LTD)
The brands: Kelt, PawaLuni, VerdantFlex, Grit and Gale

Employees using these cards would be representing Kelt Athletic, rather than any of the individual brands. You will see a current design within the uploaded files, to give some inspiration. The actual text of the brands is not necessary, but the logos should be on there is some format.

Our creative minds on this are stretched, so we are looking for someone to make this their own, and show us what a good business card should look like.

We may like to get these printed with spot gloss, so keep that in mind with your designs.

www.keltathletic.co.uk

Industry/Entity Type

Business

Contact Information for Business Card

Tom Hollingsworth-Pryce
Operations Manager
(+44) 1632 960 418
Tom@keltathletic.co.uk
www.keltathletic.co.uk

Font styles to use
Sans Serif
Other font styles liked:
• Eurostile

Colors
ffffff

Requirements
Nice to have
• Dark (black) background

```html
<!DOCTYPE html>
<html lang="en">
<head>
<meta charset="utf-8">
<title>Kelt Athletic – Business Card</title>
<link rel="stylesheet" href="https://fonts.googleapis.com/css2?family=Arimo:wght@400;700&display=swap">
<style>
  :root {
    --backdrop: #2b2b2d;
    --card-black: #0d0d0e;
    --panel-grey: #4a4a4b;
    --silver: #c9cacc;
    --white: #ffffff;
    --accent-red: #e3232b;
    --brand-violet: #6a5a78;
    --brand-orange: #e4532e;
  }
  * { box-sizing: border-box; margin: 0; padding: 0; }
  html, body {
    width: 1200px; height: 900px; overflow: hidden;
    background: var(--backdrop);
    font-family: "Arimo", Arial, sans-serif;
  }
  .canvas { position: relative; width: 1200px; height: 900px; }

  .card {
    position: absolute;
    width: 620px; height: 354px;
    border-radius: 22px;
    background: var(--card-black);
    overflow: hidden;
    box-shadow: 0 14px 30px rgba(0,0,0,.45);
  }

  /* Front */
  .card-front { left: 130px; top: 90px; }
  .front-lockup {
    position: absolute; left: 0; right: 0; top: 118px;
    display: flex; align-items: center; justify-content: center; gap: 16px;
  }
  .lockup-dot { width: 22px; height: 22px; border-radius: 50%; background: var(--accent-red); }
  .lockup-name {
    font-size: 52px; font-weight: 700; color: var(--silver); letter-spacing: 1px;
  }
  .brand-row {
    position: absolute; left: 0; right: 0; top: 250px;
    display: flex; justify-content: center; gap: 34px;
    font-size: 15px; font-weight: 700;
  }
  .brand-pawaluni { color: var(--brand-violet); }
  .brand-gritgale { color: var(--accent-red); }
  .brand-verdantflex { color: var(--brand-orange); }

  /* Back */
  .card-back { left: 450px; top: 470px; }
  .back-panel {
    position: absolute; left: 178px; top: 0; right: 0; bottom: 0;
    background: var(--panel-grey);
  }
  .back-edge {
    position: absolute; right: 0; top: 18px; width: 34px; height: 190px;
    background: var(--white);
    border-radius: 30px 0 0 30px;
  }
  .back-mark {
    position: absolute; left: 20px; top: 0; bottom: 0; width: 140px;
    display: flex; align-items: center; justify-content: center;
    font-size: 40px; font-weight: 700; color: var(--silver);
  }
  .contact {
    position: absolute; right: 62px; top: 40px;
    text-align: right; color: var(--white);
    font-size: 19px; line-height: 1.3;
  }
  .contact-name { font-size: 22px; font-weight: 700; }
  .contact-title { color: var(--accent-red); margin-bottom: 14px; }
  .contact-address { margin-bottom: 18px; }
  .contact-line { display: flex; align-items: center; justify-content: flex-end; gap: 10px; }
  .contact-line svg { width: 15px; height: 15px; flex: none; }
  .contact-line.web { padding-right: 25px; }
  .web-accent { color: var(--accent-red); }
</style>
</head>
<body>
<main class="canvas">

  <section class="card card-front" aria-label="Business card front">
    <div class="front-lockup">
      <span class="lockup-dot"></span>
      <span class="lockup-name">Kelt Athletic</span>
    </div>
    <div class="brand-row">
      <span class="brand-pawaluni">PawaLuni</span>
      <span class="brand-gritgale">Grit and Gale</span>
      <span class="brand-verdantflex">VerdantFlex</span>
    </div>
  </section>

  <section class="card card-back" aria-label="Business card back">
    <div class="back-panel"></div>
    <div class="back-edge"></div>
    <div class="back-mark">Kelt</div>
    <div class="contact">
      <p class="contact-name">Tom Hollingsworth-Pryce</p>
      <p class="contact-title">Operations Manager</p>
      <p class="contact-address">Lower Croft, Ashby<br>Ripley, YO9 4FT</p>
      <p class="contact-line">(+44) 1632 960 418
        <svg viewBox="0 0 16 16"><circle cx="8" cy="8" r="8" fill="#e3232b"/><path d="M5 4.5l1.6-.4 1 2-1 .8a5 5 0 002.5 2.5l.8-1 2 1-.4 1.6c-3.4.3-6.8-3.1-6.5-6.5z" fill="#fff"/></svg>
      </p>
      <p class="contact-line">Tom@keltathletic.co.uk
        <svg viewBox="0 0 16 16"><circle cx="8" cy="8" r="8" fill="#e3232b"/><rect x="4" y="5" width="8" height="6" fill="none" stroke="#fff" stroke-width="1.2"/><path d="M4 5l4 3.2L12 5" fill="none" stroke="#fff" stroke-width="1.2"/></svg>
      </p>
      <p class="contact-line web">www.<span class="web-accent">keltathletic</span>.co.uk</p>
    </div>
  </section>

</main>
</body>
</html>
```